Stationary for Oil & Gas Company
Valmora Engineering
Project: Stationary for Oil & Gas Company
Stationary for Oil & Gas Company - Energy
Creative Brief
Professional
Peter Hawley
Managing Director
18 Upper Fennick Road London E9 3LQ United Kingdom
peter.hawley@valmora-example.com
www.valmora-example.com
We need a design for business cards, letters, envelopes, folders and other presentation material.
Company name and/or logo

```html
<!DOCTYPE html>
<html lang="en">
<head>
<meta charset="utf-8">
<title>Valmora Engineering – Business Card</title>
<link rel="stylesheet" href="https://fonts.googleapis.com/css2?family=Michroma&family=Exo+2:wght@400;600;800&display=swap">
<style>
  :root{
    --bg:#e9ebec;
    --card:#ffffff;
    --teal:#6f9e9b;
    --teal-dark:#5b8784;
    --ink:#1f2426;
    --orange:#ef7d22;
    --muted:#4d5557;
    --white:#ffffff;
  }
  *{box-sizing:border-box;margin:0;padding:0}
  html,body{width:1200px;height:948px;overflow:hidden;background:var(--bg)}
  body{position:relative;font-family:"Exo 2",sans-serif;color:var(--ink)}

  .card{position:absolute;left:240px;width:720px;height:412px;border-radius:26px;background:var(--card);
        box-shadow:0 10px 28px rgba(0,0,0,.14);overflow:hidden}
  .card--front{top:40px}
  .card--back{top:496px}

  /* front */
  .brand{position:absolute;left:0;right:0;top:150px;text-align:center}
  .brand__name{font-family:"Michroma",sans-serif;font-size:54px;letter-spacing:2px;color:var(--ink);line-height:1}
  .brand__sub{margin-top:14px;font-family:"Michroma",sans-serif;font-size:19px;letter-spacing:13px;color:var(--orange);padding-left:13px}

  /* back */
  .band{position:absolute;left:0;right:0;top:112px;height:262px;background:var(--teal)}
  .icon-dot{position:absolute;width:52px;height:52px;border-radius:50%;background:var(--teal);display:flex;align-items:center;justify-content:center}
  .icon-dot svg{width:26px;height:26px;fill:var(--white)}
  .icon-dot--person{left:72px;top:40px}
  .icon-dot--pin{left:306px;top:40px}
  .icon-dot--phone{left:594px;top:40px}

  .info{position:absolute;color:var(--white);font-size:17px;line-height:1.35}
  .info--person{left:40px;top:128px}
  .person__name{font-size:24px;font-weight:600;letter-spacing:1px;text-transform:uppercase}
  .person__role{font-size:14px;opacity:.9}
  .info--address{left:250px;top:128px;width:190px}
  .info--phone{left:560px;top:128px;text-align:left}

  .web{position:absolute;left:40px;top:248px;display:flex;align-items:center;gap:16px;color:var(--white);font-size:15px;line-height:1.5}
  .web .icon-dot{position:static;background:var(--white)}
  .web .icon-dot svg{fill:var(--teal)}

  .links{position:absolute;left:390px;top:236px;display:flex;flex-direction:column;gap:12px}
  .link{display:flex;align-items:center;gap:14px;color:var(--white);font-size:15px}
  .link__dot{width:30px;height:30px;border-radius:50%;background:var(--white)}
</style>
</head>
<body>

<section class="card card--front" aria-label="Card front">
  <div class="brand">
    <div class="brand__name">VALMORA</div>
    <div class="brand__sub">ENGINEERING</div>
  </div>
</section>

<section class="card card--back" aria-label="Card back">
  <div class="band"></div>

  <div class="icon-dot icon-dot--person">
    <svg viewBox="0 0 24 24"><circle cx="12" cy="8" r="4.5"/><path d="M3 22c0-5 4-8 9-8s9 3 9 8z"/></svg>
  </div>
  <div class="icon-dot icon-dot--pin">
    <svg viewBox="0 0 24 24"><path d="M12 1.5a7.5 7.5 0 0 0-7.5 7.5c0 5.6 7.5 13.5 7.5 13.5s7.5-7.9 7.5-13.5A7.5 7.5 0 0 0 12 1.5zm0 10.5a3 3 0 1 1 0-6 3 3 0 0 1 0 6z"/></svg>
  </div>
  <div class="icon-dot icon-dot--phone">
    <svg viewBox="0 0 24 24"><path d="M7 1h10a2 2 0 0 1 2 2v18a2 2 0 0 1-2 2H7a2 2 0 0 1-2-2V3a2 2 0 0 1 2-2zm0 3v14h10V4zm5 15.5a1.2 1.2 0 1 0 0 2.4 1.2 1.2 0 0 0 0-2.4z"/></svg>
  </div>

  <div class="info info--person">
    <div class="person__name">Peter Hawley</div>
    <div class="person__role">Managing Director</div>
  </div>
  <div class="info info--address">18 Upper Fennick Road<br>London E9 3LQ</div>
  <div class="info info--phone">020 7946 0321<br>020 7946 0488</div>

  <div class="web">
    <div class="icon-dot">
      <svg viewBox="0 0 24 24"><path d="M2 4h20v13H2zm2 2v9h16V6zM9 19h6v2H9z"/></svg>
    </div>
    <div>peter.hawley@valmora-example.com<br>www.valmora-example.com</div>
  </div>

  <div class="links">
    <div class="link"><span class="link__dot"></span>valmora-example.com/news</div>
    <div class="link"><span class="link__dot"></span>valmora-example.com/updates</div>
    <div class="link"><span class="link__dot"></span>valmora-example.com/team</div>
  </div>
</section>

</body>
</html>
```